Postcard

I'm a realtor looking to create a general postcard for my business to be mailed out to homeowners. I have a good idea of what I'm looking for, just need someone to put it all together and make it look good. Please keep colors similar to the logo. The save money symbol can be different colors to help stand out. File #6 is the theme for the bottom section of file #5.

Realtor

```html
<!DOCTYPE html>
<html lang="en">
<head>
<meta charset="utf-8">
<title>Harlow Realty Postcard</title>
<link rel="stylesheet" href="https://fonts.googleapis.com/css2?family=Lato:wght@400;700;900&family=Oswald:wght@500;700&display=swap">
<style>
  :root {
    --royal: #1d4596;
    --royal-deep: #183b86;
    --sun: #f5d52f;
    --white: #ffffff;
    --page: #1c1c1c;
    --leaf: #5f8a3a;
    --leaf-dark: #2f4d1f;
    --lawn: #6aa33d;
    --skin: #d9b39a;
    --shirt: #ece4d3;
    --ink: #2a2a2a;
  }
  * { margin: 0; padding: 0; box-sizing: border-box; }
  html, body { width: 1200px; height: 900px; overflow: hidden; }
  body { background: var(--page); font-family: "Lato", sans-serif; position: relative; }

  .postcard {
    position: absolute; left: 100px; top: 60px;
    width: 1000px; height: 780px;
    background: var(--white);
  }

  .brand-panel {
    position: absolute; left: 5px; top: 5px; width: 645px; height: 278px;
    background: var(--royal);
    display: flex; flex-direction: column; align-items: center; justify-content: center;
  }
  .brand-name {
    color: var(--white); font-weight: 700; text-align: center;
    font-size: 96px; line-height: 1; letter-spacing: 2px;
  }
  .brand-name .brand-suffix { display: block; font-size: 46px; letter-spacing: 5px; margin-top: 26px; }

  .savings-panel {
    position: absolute; left: 660px; top: 5px; width: 335px; height: 278px;
    background: var(--sun);
    display: flex; flex-direction: column; align-items: center; justify-content: flex-end;
    padding-bottom: 20px;
  }
  .savings-symbol { width: 190px; height: 170px; border-radius: 50% 50% 46% 46%; background: var(--royal); margin-bottom: 18px; }
  .savings-label { color: var(--royal); font-weight: 900; font-size: 29px; }

  .home-photo {
    position: absolute; left: 5px; top: 293px; width: 645px; height: 482px;
    background: linear-gradient(180deg, var(--leaf-dark) 0%, var(--leaf) 45%, #b9a98c 60%, var(--lawn) 85%);
  }
  .agent-photo {
    position: absolute; left: 5px; top: 535px; width: 205px; height: 240px;
    background: linear-gradient(180deg, var(--skin) 0%, var(--skin) 65%, var(--shirt) 66%);
    border: 6px solid var(--white); border-radius: 90px 90px 0 0; border-bottom: none;
  }
  .contact-bar {
    position: absolute; left: 160px; top: 713px; width: 490px; height: 62px;
    background: var(--sun);
    display: flex; align-items: center; padding-left: 46px; gap: 8px;
    color: var(--royal);
  }
  .contact-phone { font-weight: 700; font-size: 24px; margin-right: 6px; white-space: nowrap; }
  .contact-web { font-weight: 700; font-size: 14px; letter-spacing: .2px; white-space: nowrap; }
  .contact-bar svg { flex: none; }

  .offer-panel {
    position: absolute; left: 665px; top: 293px; width: 330px; height: 482px;
    background: var(--royal);
    padding: 10px 20px 0 20px;
  }
  .rate-badge {
    background: var(--white); border-radius: 6px;
    display: flex; align-items: center; justify-content: center; gap: 6px;
    height: 84px; padding: 0 8px; overflow: hidden;
    font-family: "Oswald", sans-serif; color: var(--royal);
  }
  .rate-value { font-size: 56px; font-weight: 700; line-height: 1; letter-spacing: -1px; white-space: nowrap; }
  .rate-text { display: flex; flex-direction: column; align-items: flex-end; line-height: 1; white-space: nowrap; }
  .rate-text .rate-kicker { font-size: 19px; font-weight: 500; color: var(--ink); }
  .rate-text .rate-main { font-size: 37px; font-weight: 700; }

  .feature-list { list-style: none; margin-top: 16px; }
  .feature-list li {
    position: relative; padding-left: 17px;
    color: var(--white); font-weight: 700; font-size: 16.5px; line-height: 25px;
  }
  .feature-list li::before {
    content: ""; position: absolute; left: 0; top: 9px;
    width: 7px; height: 7px; border-radius: 50%; background: var(--sun);
  }
</style>
</head>
<body>
  <main class="postcard">
    <header class="brand-panel">
      <h1 class="brand-name">Harlow<span class="brand-suffix">REALTY, LLC</span></h1>
    </header>

    <section class="savings-panel">
      <div class="savings-symbol" role="img" aria-label="Money bag symbol with a dollar sign"></div>
      <p class="savings-label">SAVE MONEY</p>
    </section>

    <div class="home-photo" role="img" aria-label="Photograph of a gabled family home with a porch, tall trees and a landscaped front garden"></div>
    <div class="agent-photo" role="img" aria-label="Cut-out portrait of the realtor"></div>

    <div class="contact-bar">
      <svg width="22" height="22" viewBox="0 0 22 22" aria-hidden="true">
        <rect width="22" height="22" rx="4" fill="var(--royal)"/>
        <path d="M7 5c1 0 2 2.5 2 3s-1 1-1 1.5 2 3.5 3.5 4c.5 0 1-1 1.5-1s3 1 3 2-1.5 2.5-3 2.5C9 17 5 12 5 8c0-1.5 1-3 2-3z" fill="var(--sun)"/>
      </svg>
      <span class="contact-phone">555.014.2860</span>
      <svg width="20" height="20" viewBox="0 0 20 20" aria-hidden="true" fill="none" stroke="var(--royal)" stroke-width="1.5">
        <circle cx="10" cy="10" r="8.5"/>
        <ellipse cx="10" cy="10" rx="3.8" ry="8.5"/>
        <line x1="1.5" y1="10" x2="18.5" y2="10"/>
        <line x1="3" y1="5.5" x2="17" y2="5.5"/>
        <line x1="3" y1="14.5" x2="17" y2="14.5"/>
      </svg>
      <span class="contact-web">WWW.HARLOWREALTY.COM</span>
    </div>

    <section class="offer-panel">
      <div class="rate-badge">
        <span class="rate-value">3.5%</span>
        <span class="rate-text"><span class="rate-kicker">FULL SERVICE</span><span class="rate-main">LISTINGS</span></span>
      </div>
      <ul class="feature-list">
        <li>Professional Photography</li>
        <li>Full Colour Brochures</li>
        <li>Digital Floor Plans</li>
        <li>Personalized Website</li>
        <li>Featured Listings on Homefinder + Nestview</li>
        <li>Full MLS Benefits</li>
        <li>Open House</li>
        <li>Sign post in Yard</li>
        <li>Solar Power Brochure Box</li>
        <li>Additional Discount for unrepresentical buyers</li>
        <li>Expert Negotiations</li>
        <li>Much,much more!</li>
      </ul>
    </section>
  </main>
</body>
</html>
```